Business Card Design Project

I need a business card design for our new logo, please check the logo at the following link:
https://www.filecrate.net/s/q7rtx2pw9kd41m/FernLoop.png
The address on the business card:
Av. Gervásio Tavares 418 sala 207
Barra da Tijuca, Rio de Janeiro, RJ
CEP: 22714-380
Brasil
Phone: +55 21 86347215
e-mail: osvaldo@fernloop.com.br
Updates
Thank you all for sending your designs, we will not provide feedback because there are too many designs, on December 3 we will pick the best design according to our point of view. Please keep posting.
Osvaldo
Industry/Entity Type
Business
Look and feel
Each slider illustrates characteristics of the customer's brand and the style your logo design should communicate.

```html
<!DOCTYPE html>
<html lang="pt-BR">
<head>
<meta charset="utf-8">
<title>FernLoop – Cartão de Visita</title>
<link rel="stylesheet" href="https://fonts.googleapis.com/css2?family=Ubuntu:wght@400;500;700&display=swap">
<style>
  :root {
    --backdrop: #5a5f63;
    --card-black: #141414;
    --panel-white: #ffffff;
    --ink: #1c1c1c;
    --accent-yellow: #f5c400;
    --rule: #222222;
    --slot-edge: #cfcfcf;
  }
  * { margin: 0; padding: 0; box-sizing: border-box; }
  html, body {
    width: 1200px; height: 1154px; overflow: hidden;
    background: var(--backdrop);
    font-family: "Ubuntu", sans-serif;
  }
  .business-card {
    position: absolute; left: 310px; top: 93px;
    width: 580px; height: 966px;
    background: var(--card-black);
  }
  .card-panel {
    position: absolute; left: 65px; top: 64px;
    width: 450px; height: 838px;
    background: var(--panel-white);
    border-radius: 16px;
  }
  .panel-slot {
    position: absolute; left: 105px;
    width: 242px; height: 40px;
    background: var(--card-black);
    border-radius: 14px;
  }
  .panel-slot--top { top: -8px; border-bottom: 3px solid var(--slot-edge); }
  .panel-slot--bottom { bottom: -8px; border-top: 3px solid var(--slot-edge); }
  .brand-mark {
    position: absolute; left: 162px; top: 100px;
    width: 126px; height: 126px;
    border-radius: 50%;
    background: var(--accent-yellow);
  }
  .brand-name {
    position: absolute; left: 0; right: 0; top: 268px;
    text-align: center;
    font-size: 80px; line-height: 100px; font-weight: 700; letter-spacing: -1px;
    color: var(--ink);
  }
  .divider {
    position: absolute; height: 2px; background: var(--rule);
  }
  .divider--upper { left: 40px; width: 368px; top: 407px; }
  .divider--lower { left: 44px; width: 368px; top: 580px; }
  .address {
    position: absolute; left: 0; right: 0; top: 437px;
    text-align: center; font-style: normal;
    font-size: 24px; line-height: 30px; color: var(--ink);
  }
  .contact-bar {
    position: absolute; left: 22px; width: 405px;
    background: var(--card-black);
    border-radius: 5px;
    color: var(--accent-yellow);
    font-size: 20px;
  }
  .contact-bar svg { position: absolute; left: 18px; top: 50%; transform: translateY(-50%); }
  .contact-bar span { position: absolute; left: 117px; top: 50%; transform: translateY(-50%); white-space: nowrap; }
  .contact-bar--email { top: 634px; height: 43px; }
  .contact-bar--phone { top: 700px; height: 46px; }
  .contact-bar--phone span { left: 93px; }
</style>
</head>
<body>
  <div class="business-card">
    <div class="card-panel">
      <div class="panel-slot panel-slot--top"></div>

      <div class="brand-mark"></div>
      <div class="brand-name">FernLoop</div>

      <div class="divider divider--upper"></div>
      <address class="address">
        Av. Gervásio Tavares 418 sala 207<br>
        Barra da Tijuca, Rio de Janeiro, RJ<br>
        CEP: 22714-380<br>
        Brasil
      </address>
      <div class="divider divider--lower"></div>

      <div class="contact-bar contact-bar--email">
        <svg width="40" height="28" viewBox="0 0 40 28" aria-hidden="true">
          <rect x="1.5" y="1.5" width="37" height="25" fill="none" stroke="#f5c400" stroke-width="3"/>
          <polyline points="2,3 20,17 38,3" fill="none" stroke="#f5c400" stroke-width="3"/>
        </svg>
        <span>osvaldo@fernloop.com.br</span>
      </div>

      <div class="contact-bar contact-bar--phone">
        <svg width="24" height="36" viewBox="0 0 24 36" aria-hidden="true">
          <rect x="4" y="0" width="3" height="6" fill="#f5c400"/>
          <rect x="1" y="5" width="22" height="30" rx="4" fill="#f5c400"/>
          <rect x="5" y="9" width="14" height="9" fill="#141414"/>
          <rect x="5" y="22" width="4" height="3" fill="#141414"/>
          <rect x="10" y="22" width="4" height="3" fill="#141414"/>
          <rect x="15" y="22" width="4" height="3" fill="#141414"/>
          <rect x="5" y="27" width="4" height="3" fill="#141414"/>
          <rect x="10" y="27" width="4" height="3" fill="#141414"/>
          <rect x="15" y="27" width="4" height="3" fill="#141414"/>
        </svg>
        <span>+55 21 86347215</span>
      </div>

      <div class="panel-slot panel-slot--bottom"></div>
    </div>
  </div>
</body>
</html>
```